Tarnovich Family website redesign

Our family website tarnovich.com has not been updated since 2010 and desperately needs a new look that's easy to edit. The new design needs to be able to accommodate all the current sections (some text, some photos/images/gallery), although not all need to be listed in top-level tabs.

The feel of the design should be fun and colorful without being childish or cartoonish (we're almost 60!). Also, we are math and engineering types so generally prefer geometric patterns/graphics.

I've attached some logos, graphics, and business card (done through ArtHivePro) that we use in other ways and especially like the green/red hummingbird, if it can be incorporated somehow.

Target Market(s)

Family and personal friends

Font styles to use
Sans Serif

Colors

Designer to choose colors to be used in the design.

Requirements
Must have
• Photo galleries, Contact Us form, password-protected section or page-by-page
Nice to have
• Blog posts (not sure we will use this but would be nice to have the option); social media links (Kin, Lux, Pip)
Should not have
• E-commerce

```html
<!DOCTYPE html>
<html lang="en">
<head>
<meta charset="utf-8">
<title>Tarnovich Family</title>
<link href="https://fonts.googleapis.com/css2?family=Cinzel:wght@400;700&family=Open+Sans:wght@400;600;700&display=swap" rel="stylesheet">
<style>
:root{
  --blue:#1f5fa8;
  --blue-dark:#173f6e;
  --green:#7cc242;
  --green-dark:#2f6b1d;
  --tint:#eef5fb;
  --text:#3c4650;
  --muted:#8a95a0;
  --white:#ffffff;
  --line:#c8d0d8;
}
*{box-sizing:border-box;margin:0;padding:0}
html,body{width:1200px;height:3508px;overflow:hidden}
body{font-family:"Open Sans",sans-serif;color:var(--text);background:var(--white);position:relative}
.section-title{font-family:"Cinzel",serif;font-size:40px;color:var(--blue);text-align:center;letter-spacing:2px;font-weight:400}
.btn{display:inline-block;border-radius:30px;font-size:13px;font-weight:700;letter-spacing:1px;color:var(--white);text-transform:uppercase}

/* header */
.site-header{position:absolute;top:0;left:0;width:1200px;height:100px;background:var(--white)}
.brand{position:absolute;left:44px;top:22px;display:flex;align-items:center;gap:12px;font-size:36px;font-weight:700;color:var(--blue)}
.brand-dot{width:22px;height:22px;border-radius:50%;background:var(--green)}
.main-nav{position:absolute;right:56px;top:48px;display:flex;gap:28px;font-size:15px;font-weight:600;color:var(--blue)}

/* hero */
.hero{position:absolute;top:100px;left:0;width:1200px;height:690px;overflow:hidden}
.hero-photo{position:absolute;inset:0;background:
  radial-gradient(ellipse 520px 260px at 600px 470px,#8a4f3e 0%,rgba(138,79,62,0) 100%),
  radial-gradient(ellipse 380px 420px at 80px 260px,#24331f 0%,rgba(36,51,31,0) 100%),
  radial-gradient(ellipse 380px 420px at 1120px 260px,#24331f 0%,rgba(36,51,31,0) 100%),
  linear-gradient(180deg,#9fb3c6 0%,#7d8e9c 30%,#6b5148 55%,#3f5a3c 80%,#2e3f2c 100%)}
.hero-shade{position:absolute;inset:0;background:rgba(10,20,35,.3)}
.hero-copy{position:absolute;top:150px;left:0;width:1200px;text-align:center;color:var(--white)}
.hero-copy h1{font-family:"Cinzel",serif;font-weight:400;font-size:50px;line-height:1.15;letter-spacing:2px}
.hero-copy h1 strong{font-weight:700;display:block;font-size:46px}
.hero-copy p{margin:26px auto 0;width:840px;font-size:20px;line-height:1.5}
.hero-copy .btn{margin-top:40px;background:var(--green-dark);padding:14px 30px}
.hero-arrow{position:absolute;top:320px}
.hero-arrow.left{left:30px}.hero-arrow.right{right:30px}
.hero-wave{position:absolute;bottom:0;left:0}

/* about */
.about{position:absolute;top:790px;left:0;width:1200px;height:440px}
.about-copy{position:absolute;left:112px;top:40px;width:560px}
.about-copy h2{font-family:"Cinzel",serif;font-weight:400;font-size:44px;color:var(--blue);letter-spacing:2px}
.about-lead{margin-top:20px;font-size:22px;line-height:1.4;color:var(--blue-dark)}
.about-body{margin-top:18px;font-size:14px;line-height:1.6;color:var(--muted)}
.about-copy .btn{margin-top:22px;background:var(--green);padding:14px 30px}
.about-art{position:absolute;left:700px;top:30px;width:320px;height:300px;border-radius:50%;background:
  radial-gradient(circle at 62% 38%,#c8343a 0 14%,rgba(200,52,58,0) 26%),
  radial-gradient(circle at 50% 50%,#3e8a2e 0%,#8cc56b 45%,rgba(255,255,255,0) 72%)}

/* news */
.news{position:absolute;top:1240px;left:0;width:1200px;height:400px;background:var(--tint)}
.news .section-title{position:absolute;top:44px;width:100%}
.news-list{position:absolute;top:140px;left:110px;display:flex;gap:16px}
.news-card{width:234px;height:192px;background:var(--white);border:1px solid #d6e2ee;position:relative}
.news-date{position:absolute;left:14px;top:10px;background:var(--blue);color:var(--white);font-size:12px;font-weight:700;padding:6px 10px}
.news-text{position:absolute;left:30px;top:58px;right:20px;font-size:13px;line-height:1.45}
.news-card .btn{position:absolute;left:30px;bottom:22px;background:var(--green-dark);font-size:11px;padding:8px 16px}
.news-dots{position:absolute;top:388px;left:0;width:100%;display:flex;justify-content:center;gap:8px;transform:translateY(-30px)}
.news-dots span{width:8px;height:8px;border-radius:50%;background:#c7d3df}
.news-dots span.on{background:var(--blue)}

/* cards */
.cards{position:absolute;top:1640px;left:0;width:1200px;height:520px}
.cards .section-title{position:absolute;top:120px;width:100%}
.cards-row{position:absolute;top:208px;left:112px;display:flex;gap:30px}
.card-item{width:222px;text-align:center}
.card-photo{height:192px;border:3px solid var(--white);box-shadow:0 2px 8px rgba(0,0,0,.15)}
.card-year{margin-top:22px;font-size:20px;font-weight:600;color:var(--text)}
.slider-arrow{position:absolute;top:290px}
.slider-arrow.left{left:30px}.slider-arrow.right{right:30px}

/* gallery */
.gallery{position:absolute;top:2160px;left:0;width:1200px;height:820px;background:var(--tint)}
.gallery .section-title{position:absolute;top:52px;width:100%}
.gallery-grid{position:absolute;top:144px;left:160px;display:grid;grid-template-columns:260px 320px 316px;grid-auto-rows:236px;gap:12px}
.gallery-grid div{border-radius:2px}
.gallery .btn{position:absolute;top:728px;left:520px;background:var(--green-dark);padding:14px 32px}

/* password */
.members{position:absolute;top:2980px;left:0;width:1200px;height:230px;overflow:hidden}
.members-photo{position:absolute;inset:0;background:
  radial-gradient(ellipse 300px 120px at 620px 210px,#6b7a3a 0%,rgba(107,122,58,0) 100%),
  radial-gradient(ellipse 200px 200px at 120px 100px,#7a4a3a 0%,rgba(122,74,58,0) 100%),
  radial-gradient(ellipse 200px 200px at 1080px 120px,#3a5a7a 0%,rgba(58,90,122,0) 100%),
  linear-gradient(90deg,#3b4652,#5a4a42 50%,#2f3d48)}
.members-shade{position:absolute;inset:0;background:rgba(15,25,38,.55)}
.members h2{position:absolute;top:58px;width:100%;text-align:center;font-family:"Cinzel",serif;font-weight:400;font-size:32px;color:var(--white);letter-spacing:2px}
.members-form{position:absolute;top:122px;left:280px;display:flex}
.members-input{width:560px;height:48px;background:var(--white);font-size:14px;color:var(--muted);padding:14px 18px}
.members-go{width:56px;height:48px;background:var(--green-dark);color:var(--white);font-weight:700;font-size:15px;text-align:center;line-height:48px}

/* footer */
.site-footer{position:absolute;top:3210px;left:0;width:1200px;height:298px;background:var(--white);text-align:center}
.social{position:absolute;top:60px;left:0;width:100%;display:flex;justify-content:center;gap:14px}
.social span{width:46px;height:46px;border-radius:50%;border:2px solid var(--line);font-size:12px;font-weight:600;color:var(--text);line-height:42px}
.footer-links{position:absolute;top:140px;width:100%;display:flex;justify-content:center;gap:26px;font-size:13px;color:var(--text)}
.copyright{position:absolute;top:180px;width:100%;font-size:13px;color:var(--muted)}
</style>
</head>
<body>

<header class="site-header">
  <div class="brand"><span class="brand-dot"></span>Dana &amp; Taz</div>
  <nav class="main-nav">
    <span>Christmas Cards</span><span>Kids</span><span>What's New</span><span>Fun &amp; Games</span><span>Photo Album</span>
  </nav>
</header>

<section class="hero">
  <div class="hero-photo" role="img" aria-label="Family brick home at dusk framed by trees"></div>
  <div class="hero-shade"></div>
  <div class="hero-copy">
    <h1>Welcome to<strong>The Tarnovich Family website</strong></h1>
    <p>All of our Christmas picture cards (starting in the year we were married, 1981) are now available. All Holiday letters (starting in 1989) are now available.</p>
    <span class="btn">View Gallery</span>
  </div>
  <svg class="hero-arrow left" width="30" height="50" viewBox="0 0 30 50"><path d="M24 4 L6 25 L24 46" fill="none" stroke="#fff" stroke-width="4"/></svg>
  <svg class="hero-arrow right" width="30" height="50" viewBox="0 0 30 50"><path d="M6 4 L24 25 L6 46" fill="none" stroke="#fff" stroke-width="4"/></svg>
  <svg class="hero-wave" width="1200" height="110" viewBox="0 0 1200 110">
    <path d="M0 40 C300 110 600 -10 900 30 C1030 48 1120 40 1200 20 L1200 110 L0 110 Z" fill="#2f6b1d"/>
    <path d="M0 62 C300 120 600 20 900 52 C1030 66 1120 58 1200 42 L1200 110 L0 110 Z" fill="#1f5fa8"/>
    <path d="M0 80 C300 130 600 45 900 72 C1030 84 1120 78 1200 66 L1200 110 L0 110 Z" fill="#ffffff"/>
  </svg>
</section>

<section class="about">
  <div class="about-copy">
    <h2>About Us</h2>
    <p class="about-lead">Morbi eget arcu Morbi porta libero id ullamcorper nonummy nibh ligula pulvinar metus eget</p>
    <p class="about-body">Maecenas porttitor purus nisi eleifend libero a tempus libero lectus feugiat felis. Morbi diam ornare viverra in gravida eu mattis in amet. Morbi eget arcu porta libero id ullamcorper.</p>
    <span class="btn">Contact Us</span>
  </div>
  <div class="about-art" role="img" aria-label="Green and red hummingbird illustration"></div>
</section>

<section class="news">
  <h2 class="section-title">What's New</h2>
  <div class="news-list">
    <article class="news-card"><span class="news-date">12/14/03</span><p class="news-text">Christmas card and holiday letter for 2003 now available.</p><span class="btn">Read More</span></article>
    <article class="news-card"><span class="news-date">12/10/03</span><p class="news-text">(321 photo album from our June 2003 China trip.</p><span class="btn">Read More</span></article>
    <article class="news-card"><span class="news-date">10/20/03</span><p class="news-text">My mother passed away today.</p><span class="btn">Read More</span></article>
    <article class="news-card"><span class="news-date">10/05/03</span><p class="news-text">Added a few new pictures.</p><span class="btn">Read More</span></article>
  </div>
  <div class="news-dots"><span></span><span class="on"></span><span></span><span></span><span></span><span></span><span></span></div>
</section>

<section class="cards">
  <h2 class="section-title">Christmas Cards</h2>
  <svg class="slider-arrow left" width="40" height="40" viewBox="0 0 40 40"><circle cx="20" cy="20" r="18" fill="#fff" stroke="#c8d0d8" stroke-width="2"/><path d="M23 12 L15 20 L23 28" fill="none" stroke="#3c4650" stroke-width="3"/></svg>
  <div class="cards-row">
    <div class="card-item"><div class="card-photo" role="img" aria-label="2010 family Christmas card group photo" style="background:radial-gradient(ellipse at 50% 70%,#2a3240 0%,rgba(42,50,64,0) 60%),linear-gradient(180deg,#8ea2b6,#4f5e70 60%,#262d38)"></div><div class="card-year">2010</div></div>
    <div class="card-item"><div class="card-photo" role="img" aria-label="2009 Happy Holidays card" style="background:radial-gradient(ellipse at 30% 80%,#2f5a3a 0%,rgba(47,90,58,0) 60%),linear-gradient(160deg,#c4473e,#8e2c2a 55%,#3d5a3a)"></div><div class="card-year">2009</div></div>
    <div class="card-item"><div class="card-photo" role="img" aria-label="2008 family Christmas card photo" style="background:radial-gradient(ellipse at 60% 50%,#8a7a68 0%,rgba(138,122,104,0) 60%),linear-gradient(160deg,#4a4540,#1f1f24)"></div><div class="card-year">2008</div></div>
    <div class="card-item"><div class="card-photo" role="img" aria-label="2007 family holiday card photo" style="background:radial-gradient(ellipse at 50% 65%,#c0a088 0%,rgba(192,160,136,0) 60%),linear-gradient(180deg,#c9d6e4,#8aa0b8 50%,#f2f2f2)"></div><div class="card-year">2007</div></div>
  </div>
  <svg class="slider-arrow right" width="40" height="40" viewBox="0 0 40 40"><circle cx="20" cy="20" r="18" fill="#fff" stroke="#c8d0d8" stroke-width="2"/><path d="M17 12 L25 20 L17 28" fill="none" stroke="#3c4650" stroke-width="3"/></svg>
</section>

<section class="gallery">
  <h2 class="section-title">Photo Gallery</h2>
  <div class="gallery-grid">
    <div role="img" aria-label="Playing pool in the game room" style="background:radial-gradient(ellipse at 55% 70%,#2f6a3a 0%,rgba(47,106,58,0) 55%),linear-gradient(160deg,#6f8aa0,#3a4a5a 60%,#2a3530)"></div>
    <div role="img" aria-label="Family member smiling at a gathering" style="background:radial-gradient(ellipse at 50% 60%,#d8b8a0 0%,rgba(216,184,160,0) 45%),linear-gradient(160deg,#9ab0c6,#6a7a68 60%,#4a5a48)"></div>
    <div role="img" aria-label="Child swimming in a pool" style="background:radial-gradient(ellipse at 45% 45%,#e0b89a 0%,rgba(224,184,154,0) 30%),linear-gradient(180deg,#7fc6e0,#3f9ec4 55%,#2d7a9c)"></div>
    <div role="img" aria-label="Family with bikes outdoors" style="background:radial-gradient(ellipse at 50% 80%,#b0383a 0%,rgba(176,56,58,0) 55%),linear-gradient(180deg,#a6c4d8,#7e9a6a 50%,#5a6a50)"></div>
    <div role="img" aria-label="Riding bicycles down the street" style="background:radial-gradient(ellipse at 50% 55%,#7a3a5a 0%,rgba(122,58,90,0) 40%),linear-gradient(180deg,#6f8a5a,#8a8478 60%,#6a6a6a)"></div>
    <div role="img" aria-label="Kids playing a game indoors" style="background:radial-gradient(ellipse at 40% 60%,#c8a890 0%,rgba(200,168,144,0) 45%),linear-gradient(160deg,#dfe4ea,#8a94a4 55%,#4a5a72)"></div>
  </div>
  <span class="btn">View More</span>
</section>

<section class="members">
  <div class="members-photo" role="img" aria-label="Family playing a board game together"></div>
  <div class="members-shade"></div>
  <h2>Enter Password to get the news</h2>
  <div class="members-form"><div class="members-input">Password</div><div class="members-go">GO</div></div>
</section>

<footer class="site-footer">
  <div class="social"><span>Kin</span><span>Pip</span><span>Lux</span></div>
  <div class="footer-links"><span>About</span><span>Support</span><span>Sitemap</span><span>Terms Of Use</span><span>Privacy Statement</span></div>
  <p class="copyright">Copyright © 2018, Dana &amp; Taz. All rights reserved.</p>
</footer>

</body>
</html>
```